Bref créative
Business Cards and Letterhead
85 mm x 55 mm / DIN A4 210 mm × 297 mm
Professional
Dominik R. Hartl
Lindenweg 7, 14471 Potsdam
info@lbr-planung.example
www.lbr-planung.example
Please use the standard german sizes for business cards and letters:
85 mm x 55 mm
DIN A4: 210 mm × 297 mm

```html
<!DOCTYPE html>
<html lang="de">
<head>
<meta charset="utf-8">
<title>lbrplanung – Visitenkarten</title>
<link rel="stylesheet" href="https://fonts.googleapis.com/css2?family=Arimo:wght@400;700&display=swap">
<style>
:root{
  --stage:#2e2e2e;
  --ink:#111111;
  --paper:#ffffff;
  --orange:#f7931e;
  --orange-soft:#fbb464;
  --ghost:#e9e9e9;
  --text:#222222;
}
*{margin:0;padding:0;box-sizing:border-box}
html,body{width:1200px;height:1052px;overflow:hidden;background:var(--stage)}
body{position:relative;font-family:"Arimo",Arial,sans-serif;color:var(--text)}
.card{position:absolute;width:454px;height:270px;border-radius:14px;overflow:hidden;background:var(--paper);box-shadow:0 6px 18px rgba(0,0,0,.45)}
.card svg.card-shapes{position:absolute;inset:0}
.front-a{left:134px;top:100px}
.front-b{left:134px;top:392px}
.back-a{left:610px;top:100px}
.back-b{left:610px;top:392px}
.back-orange{left:355px;top:682px;width:483px;height:270px;background:var(--orange)}
.wordmark{position:absolute;display:flex;align-items:center;gap:8px;font-weight:700;letter-spacing:.5px}
.wordmark .dot{width:12px;height:12px;background:var(--orange)}
.front .wordmark{left:18px;top:36px;font-size:22px;color:var(--ink)}
.holder{position:absolute;right:22px;top:22px;color:var(--paper);font-weight:700;font-size:21px}
.details{position:absolute;left:26px;font-size:13px;line-height:18px;color:var(--text)}
.details.col-right{left:246px}
.front-a .details{top:148px}
.front-b .details{top:152px;font-size:10.5px;line-height:13.5px}
.web{position:absolute;right:20px;bottom:6px;font-size:13px;color:var(--orange)}
.ghost-name{position:absolute;font-weight:700;color:var(--ghost);white-space:nowrap}
.front .ghost-name{right:-10px;top:4px;font-size:64px;color:rgba(255,255,255,.08)}
.back-a .ghost-name,.back-b .ghost-name{left:110px;top:24px;font-size:78px}
.back-orange .ghost-name{left:140px;top:14px;font-size:86px;color:var(--orange-soft)}
.back-a .wordmark{left:200px;top:160px;font-size:22px;color:var(--ink)}
.back-b .wordmark{left:150px;top:112px;font-size:34px;color:var(--ink)}
.back-b .wordmark .dot{width:18px;height:18px}
.back-orange .wordmark{left:160px;top:112px;font-size:34px;color:var(--paper)}
.back-orange .wordmark .dot{width:18px;height:18px;background:var(--paper)}
</style>
</head>
<body>

<section class="card front front-a">
  <svg class="card-shapes" width="454" height="270" viewBox="0 0 454 270">
    <rect x="0" y="0" width="454" height="62" fill="var(--ink)"/>
    <path d="M0 0 H150 Q162 0 162 14 V86 L150 98 H0 Z" fill="var(--paper)"/>
    <path d="M0 98 H150 L162 86 V112 H0 Z" fill="var(--orange)"/>
    <path d="M0 230 H454 V242 H0 Z" fill="var(--orange)"/>
    <path d="M0 242 H454 V270 H0 Z" fill="var(--ink)"/>
  </svg>
  <div class="ghost-name">lbr</div>
  <div class="wordmark"><span class="dot"></span>lbrplanung</div>
  <div class="holder">Dominik R. Hartl</div>
  <div class="details">Lindenweg 7, 14471 Potsdam<br><br>Fax: (0331) 555 01 20-9<br>Email: info@lbr-planung.example</div>
  <div class="details col-right" style="top:184px">Phone: (0331) 555 01 20-0<br>Cell: (0170) 555 08 14</div>
  <div class="web">Web: www.lbr-planung.example</div>
</section>

<section class="card front front-b">
  <svg class="card-shapes" width="454" height="270" viewBox="0 0 454 270">
    <rect x="0" y="0" width="454" height="62" fill="var(--ink)"/>
    <path d="M0 0 H150 Q162 0 162 14 V86 L150 98 H0 Z" fill="var(--paper)"/>
    <path d="M0 98 H150 L162 86 V112 H0 Z" fill="var(--orange)"/>
    <path d="M0 230 H454 V242 H0 Z" fill="var(--orange)"/>
    <path d="M0 242 H454 V270 H0 Z" fill="var(--ink)"/>
  </svg>
  <div class="ghost-name">lbr</div>
  <div class="wordmark"><span class="dot"></span>lbrplanung</div>
  <div class="holder">Dominik R. Hartl</div>
  <div class="details">Lindenweg 7, 14471 Potsdam<br>Phone: (0331) 555 01 20-0<br>Cell: (0170) 555 08 14<br>Fax: (0331) 555 01 20-9<br>Email: info@lbr-planung.example</div>
  <div class="web">Web: www.lbr-planung.example</div>
</section>

<section class="card back-a">
  <div class="ghost-name">lbr</div>
  <div class="wordmark"><span class="dot"></span>lbrplanung</div>
</section>

<section class="card back-b">
  <div class="ghost-name">lbr</div>
  <div class="wordmark"><span class="dot"></span>lbrplanung</div>
</section>

<section class="card back-orange">
  <div class="ghost-name">lbr</div>
  <div class="wordmark"><span class="dot"></span>lbrplanung</div>
</section>

</body>
</html>
```